Front and content page design for Fitness Cookbook

I am looking for someone to Design a front cover for a Recipe book and also create an amazing layout for the book.

Its for a corporate seminar so has to be eye catching, professional and bold.

Content is complete

Target Market(s)

Industry/Entity Type

Health And Wellness

Font styles to use
Sans Serif

Requirements
Must have
• Eye catching, professional and bold.
• By Dorian as stated on the document
• Must have Velmora Athletics Logo on it.

```html
<!DOCTYPE html>
<html lang="en">
<head>
<meta charset="utf-8">
<title>Baked Salmon and Sautéed Red Cabbage</title>
<link rel="stylesheet" href="https://fonts.googleapis.com/css2?family=Lato:wght@400;700&display=swap">
<style>
  :root {
    --orange: #f7931e;
    --ink: #3a3a3a;
    --paper: #ffffff;
    --brand: #2f6db5;
    --photo-top: #7c6a63;
    --photo-mid: #b98a6a;
    --photo-low: #9a8f8c;
  }
  * { box-sizing: border-box; margin: 0; padding: 0; }
  html, body { width: 849px; height: 1200px; overflow: hidden; background: var(--paper); }
  body { font-family: "Lato", Arial, sans-serif; color: var(--ink); }
  .page { position: relative; width: 849px; height: 1200px; background: var(--paper); }
  .recipe-photo {
    position: absolute; left: 0; top: 0; width: 849px; height: 467px;
    background: linear-gradient(160deg, var(--photo-top) 0%, #8b5a7a 30%, var(--photo-mid) 60%, var(--photo-low) 100%);
  }
  .title-band {
    position: absolute; left: 0; top: 467px; width: 849px; height: 198px;
    background: var(--orange);
    display: flex; align-items: center; justify-content: center;
  }
  .recipe-title {
    color: var(--paper); font-weight: 400; font-size: 40px; line-height: 1.12;
    text-align: center;
  }
  .recipe-body { position: absolute; left: 51px; top: 680px; width: 750px; font-size: 15.5px; line-height: 1.3; }
  .label { color: var(--orange); font-weight: 700; text-transform: uppercase; letter-spacing: 0.3px; }
  .timing p { margin: 0; }
  .section-head { color: var(--orange); font-weight: 700; text-transform: uppercase; margin-top: 18px; letter-spacing: 0.3px; }
  .ingredients { list-style: none; }
  .instructions { margin-top: 0; }
  .footer { position: absolute; right: 40px; bottom: 36px; display: flex; align-items: center; gap: 8px; font-size: 13px; }
  .brand { display: flex; align-items: center; gap: 5px; color: var(--brand); font-weight: 700; }
  .brand-mark { width: 9px; height: 9px; background: var(--brand); }
  .page-number { color: var(--ink); margin-left: 14px; }
</style>
</head>
<body>
  <main class="page">
    <div class="recipe-photo" role="img" aria-label="Photo of a baked herb-crusted salmon fillet beside sautéed red cabbage with onion and chilli"></div>

    <header class="title-band">
      <h1 class="recipe-title">Baked Salmon and Sautéed<br>Red Cabbage</h1>
    </header>

    <section class="recipe-body">
      <div class="timing">
        <p><span class="label">Prep time</span> 5 mins</p>
        <p><span class="label">Cooking time</span> 15 mins</p>
      </div>

      <h2 class="section-head">Ingredients</h2>
      <ul class="ingredients">
        <li>200g Salmon fillet</li>
        <li>Optional seasoning for salmon: Salt, pepper, mixed herbs and chilli flakes</li>
        <li>1 tsp coconut oil or grass fed butter</li>
        <li>1 cup red cabbage</li>
        <li>1/4 white onion</li>
        <li>1 fresh red chilli</li>
        <li>Season salmon and bake in the oven for 12-15 minutes at 190°C/374°F</li>
      </ul>

      <h2 class="section-head">Cooking instructions</h2>
      <p class="instructions">Whilst cooking melt the coconut oil/butter in the pan, add the red cabbage and saute for 3-4 minutes. Add the onion and chopped up red chilli and continue to cook and mix till onion and cabbage starts to brown. Serve beside salmon.</p>
    </section>

    <footer class="footer">
      <span class="brand"><span class="brand-mark"></span>Velmora Athletics</span>
      <span class="page-number">7</span>
    </footer>
  </main>
</body>
</html>
```